Cybersecurity Start-Up - Velorix

We need a MS Word Template for everyday documents. This would be leveraged to create reports, marketing materials, internal memos etc.

The document should follow the standard MS Word template format and have an H1,H2,H3, paragraph, Title, bold font, regular font, table etc. All editable with normal MS Word features.

Our logo is also attached. We would like to see the same color scheme used throughout the document. Additional attached is a sample word document that outlines all of the components we would like to see in the template.

Requirements
Must have
• - Submission must meet all standard MS Word Template requirements.
• - Submission should make use of Built in MS Styles so as the user of the template I should be able to create a brand new page and insert an H1 for example and be able to select from the styles drop down the same font/color/style that you have designed for your submission.
• - All sections in the provided document need to be contained in your submission.
• - The table of contents should auto update if I add a new page, heading, section etc.
• - Need to read and understand all of my comments which I have placed in the sample document uploaded to the briefing
Should not have
• no fixed textboxes or image boxes. everything needs to be smoothly editable in MS Word. "Editable" means more than just being able to alter text.

```html
<!DOCTYPE html>
<html lang="en">
<head>
<meta charset="utf-8">
<title>Velorix Document Template – Page Overview</title>
<link href="https://fonts.googleapis.com/css2?family=Open+Sans:ital,wght@0,400;0,600;0,700;1,400&display=swap" rel="stylesheet">
<style>
:root{
  --stage:#cbcbcb;
  --paper:#ffffff;
  --orange:#f15a29;
  --orange-deep:#ee4a23;
  --amber:#f7941d;
  --gold:#fbb03b;
  --navy:#1f2b46;
  --ink:#333333;
  --muted:#8c8c8c;
  --grey-fill:#a7a7a7;
  --row:#f2f2f2;
  --row-alt:#e4e4e4;
  --rule:#f7b39a;
}
*{box-sizing:border-box;margin:0;padding:0}
html,body{width:1200px;height:1200px;overflow:hidden;background:var(--stage);font-family:"Open Sans",Arial,sans-serif;color:var(--ink)}
.sheet{position:relative;width:1200px;height:1200px}
.page{position:absolute;width:250px;height:354px;background:var(--paper);box-shadow:0 1px 4px rgba(0,0,0,.25);overflow:hidden}
.col-1{left:38px}.col-2{left:330px}.col-3{left:622px}.col-4{left:914px}
.row-1{top:34px}.row-2{top:420px}.row-3{top:806px}

.page-title{position:absolute;top:22px;left:28px;right:28px;text-align:center;font-size:8.4px;font-weight:400;letter-spacing:.2px;color:var(--ink);padding-bottom:4px;border-bottom:.6px solid var(--rule)}
.page-body{position:absolute;top:44px;left:28px;right:28px;font-size:3.3px;line-height:1.55}
.page-body p{margin-bottom:3px}
.h2{font-size:6.2px;color:var(--ink);margin:3px 0 1px;font-weight:400}
.h3{font-size:3.9px;color:var(--orange);margin:2px 0 1px;font-weight:400}
.lead{color:var(--orange);font-size:4.4px;line-height:1.35;margin-bottom:3px}
.lead-bold{color:var(--orange);font-weight:700;font-size:4.2px;line-height:1.4}
.italic{font-style:italic}
.justify{text-align:justify}

.page-footer{position:absolute;left:0;right:0;bottom:6px;height:7px}
.footer-band{position:absolute;left:0;top:0;width:80px;height:7px;background:var(--orange);color:#fff;font-size:2.6px;line-height:7px;padding-left:25px}
.footer-mark{position:absolute;left:96px;top:0;font-size:5px;font-weight:700;color:var(--navy);line-height:7px}
.footer-mark::after{content:"";display:inline-block;width:3px;height:3px;background:var(--orange);margin-left:1px;vertical-align:middle}
.page-num{position:absolute;right:14px;top:0;font-size:3.4px;line-height:7px}

.cover-art{position:absolute;inset:0}
.brand{position:absolute;font-weight:700;color:var(--navy);letter-spacing:-.3px}
.brand-dot{position:absolute;background:var(--orange)}

.toc-heading{color:var(--orange);font-size:5.8px;font-weight:600;margin-bottom:6px}
.toc-line{display:flex;align-items:baseline;font-size:3.4px;margin-bottom:2.2px}
.toc-line .dots{flex:1;border-bottom:.4px dotted #777;margin:0 3px}

.mission-banner{display:flex;align-items:center;background:var(--orange);color:#fff;height:22px;margin-bottom:5px;font-size:3.6px;line-height:1.3}
.mission-banner svg{flex:0 0 26px;height:22px}
.mission-banner span{padding:0 5px}

.bullet{padding-left:3px;margin-bottom:1.6px}
.bullet::before{content:"■ ";color:var(--navy);font-size:2.6px}
.sub-bullet{padding-left:20px;margin-bottom:1.4px}
.sub-bullet::before{content:"▶ ";font-size:2.6px}

.chart-title{text-align:center;font-size:5.4px;line-height:1.3;margin-bottom:2px}
.legend{text-align:center;font-size:2.6px;margin-bottom:2px}
.legend i{display:inline-block;width:2.5px;height:2.5px;margin:0 1px 0 3px}

.photo{background:linear-gradient(135deg,#dcd3c6 0%,#6c7380 55%,#2c3445 100%)}

.budget{width:100%;border-collapse:separate;border-spacing:1px;font-size:2.6px;margin:3px 0 6px}
.budget th{background:var(--orange);color:#fff;font-weight:600;padding:.6px 2px;text-align:center}
.budget td{background:var(--row);padding:.6px 3px}
.budget td.c{text-align:center}
.budget tr.sub td{background:var(--row-alt)}
.budget tr.total td{background:#d8d8d8;color:var(--orange)}
.budget tr.total td.hi{background:var(--amber);color:#fff}

.contact{position:absolute;font-size:2.4px;line-height:1.5;color:var(--ink)}
.icon-dot{display:inline-block;width:3px;height:3px;border-radius:50%;background:var(--orange);margin-right:2px;vertical-align:middle}
</style>
</head>
<body>
<main class="sheet">

  <section class="page col-1 row-1 cover">
    <svg class="cover-art" viewBox="0 0 250 354" width="250" height="354" aria-hidden="true">
      <defs>
        <linearGradient id="coverGrad" x1="0" y1="0" x2="0" y2="1">
          <stop offset="0" stop-color="#f36b2c"/>
          <stop offset="1" stop-color="#ee4a23"/>
        </linearGradient>
      </defs>
      <rect width="250" height="354" fill="#ffffff"/>
      <polygon points="0,0 250,0 250,238 0,286" fill="#f7941d"/>
      <polygon points="0,0 250,0 250,192 0,284" fill="url(#coverGrad)"/>
    </svg>
    <div class="brand" style="left:104px;top:290px;font-size:19px">Velorix</div>
    <div class="brand-dot" style="left:196px;top:298px;width:7px;height:7px"></div>
  </section>

  <section class="page col-2 row-1">
    <h1 class="page-title">TABLE OF CONTENTS</h1>
    <div class="page-body" style="top:52px">
      <div class="toc-heading">Contents</div>
      <div class="toc-line"><span>Table of Contents</span><span class="dots"></span><span>01</span></div>
      <div class="toc-line"><span>Executive Summary</span><span class="dots"></span><span>02</span></div>
      <div class="toc-line"><span>Our Understanding of Your Needs</span><span class="dots"></span><span>02</span></div>
      <div class="toc-line"><span>Our Recommendations</span><span class="dots"></span><span>03</span></div>
      <div class="toc-line"><span>Our Approach</span><span class="dots"></span><span>05</span></div>
      <div class="toc-line"><span>Budget and Timeframe</span><span class="dots"></span><span>07</span></div>
      <div class="toc-line"><span>Appendix A: About Harbor Lane</span><span class="dots"></span><span>10</span></div>
      <div class="toc-line"><span>Appendix B: Selected Client List</span><span class="dots"></span><span>10</span></div>
      <div class="toc-line"><span>Appendix C: Our Capabilities</span><span class="dots"></span><span>11</span></div>
      <div class="toc-line"><span>Appendix D: Our Process</span><span class="dots"></span><span>12</span></div>
    </div>
    <footer class="page-footer"><div class="footer-band">www.velorix.example</div><div class="footer-mark">Velorix</div><div class="page-num">1</div></footer>
  </section>

  <section class="page col-3 row-1">
    <h1 class="page-title">VISION</h1>
    <div class="page-body">
      <div class="mission-banner">
        <svg viewBox="0 0 26 22" aria-hidden="true"><circle cx="13" cy="11" r="8" fill="none" stroke="#fff" stroke-width="1.2"/><circle cx="13" cy="11" r="5" fill="none" stroke="#fbb03b" stroke-width="1.2"/><circle cx="13" cy="11" r="2" fill="#fff"/></svg>
        <span>Tallyvo's mission is to help and support the self-employed and small business owners with their administrative tasks so they can focus on what matters – their business.</span>
      </div>
      <p class="italic">Administrative tasks are cumbersome, time-consuming and often prevent small owners from focusing their time and energy on their business and their customers. They can also be extremely stressful for those attempting these tasks for the first time.</p>
      <p>At Tallyvo, we envisage accounting for the self-employed and small business owners as being automated and decentralized.</p>
      <p>Accounting can and should be done automatically. By connecting to all sources of accounting data such as bank accounts, payment systems, e-commerce websites and invoicing systems, Tallyvo AI automatically completes these tasks, which would take hours to do manually. Bookings are created automatically and statements are available within a couple of clicks.</p>
      <p>What may seem like a pipedream to the millions of self-employed who struggle with their admin is already a reality. Now is the time to join Tallyvo on its mission to transform the world of bookkeeping through the power of AI.</p>
      <div class="h2">The Tallyvo model</div>
      <p>Tallyvo is based on an innovative license model that uses Token-as-a-License (TaaL). The token represents lifelong software license for Tallyvo solutions. The pre-ICO token sale will enable Tallyvo to complete its development of Tallyvo AI to deliver fully automatic bookkeeping.</p>
      <p>The pre-ICO token sale will also pave the way for a future Tallyvo ICO. Tallyvo will launch accounting on the blockchain and ensure your accounting data is comprehensive and private, but available everywhere within your preferred apps. Furthermore, a new range of business apps will connect to Tallyvo.</p>
      <p>Tallyvo supports strong data ownership laws that truly protect individuals and ensure they have complete ownership of their data. Through decentralisation Tallyvo helps to ensure you always have full ownership of your data.</p>
      <p>To find out more about the Tallyvo AI project and the Tallyvo TaaL, please register with your email at <span style="color:#2a5db0;text-decoration:underline">www.tallyvo.example/ico</span> so we can keep you informed.</p>
    </div>
    <footer class="page-footer"><div class="footer-band">www.velorix.example</div><div class="footer-mark">Velorix</div><div class="page-num">1</div></footer>
  </section>

  <section class="page col-4 row-1">
    <h1 class="page-title">HEADLINE HERE</h1>
    <div class="page-body">
      <div class="h2">Solution</div>
      <div class="h3">AI automated accounting</div>
      <p>Tallyvo builds automation in stages on top of its current system to reach full automation thanks to the Tallyvo AI. Tallyvo AI automates every manual task performed by the user. It starts by connecting to all sources of accounting data such as bank accounts, credit card, webshop or document management systems (FolderKeep or Cratebin). Based on these data, Tallyvo AI creates bookings and generates financial reports. Finally, Tallyvo AI features chat-like interface that allows users to communicate seamlessly with it, viewing it as a trusted advisor over time for all their accounting queries.</p>
      <div class="h3">Blockchain software license or Token-as-a-License (TaaL)</div>
      <p>It is possible to create tokens on blockchain that represent software licenses, also known as Token-as-a-Licence (TaaL). Tallyvo creates TaaL by using the Quillchain official wallet which interacts with the Quillchain blockchain. Upon purchase of TaaL, the token holder is free to transfer or sell TaaL using secondary market that is built directly over the blockchain, in our case the Quillchain marketplace. Tallyvo checks the validity of a token against the blockchain ensuring that token holders have access to the software. TaaL make distribution easier for software developers. All in all, TaaL has a higher value as a normal software license.</p>
      <div class="h2">Pre-ICO Token sale</div>
      <p>To realize this innovative vision, Tallyvo is launching a pre-ICO in form of a token sale on Quillchain blockchain. 20,000,000 tokens are available to purchase for the price of CHF 0.10 each during a 30-day period to be announced. Tokens represent Tallyvo lifelong software licenses and by purchasing enough tokens, holders gain access to Tallyvo software. Future customers will still have the opportunity to buy directly yearly or monthly subscriptions to have access to Tallyvo.</p>
      <div class="h2">Future plans</div>
      <p>A future ICO is planned between 18 and 24 months after the pre-ICO token sale. This offering will support the development of Tallyvo into a fully decentralized, privacy-focused ecosystem of applications. The new model will reward each participant so that a new world with zero administrative tasks becomes reality.</p>
    </div>
    <footer class="page-footer"><div class="footer-band">www.velorix.example</div><div class="footer-mark">Velorix</div><div class="page-num">1</div></footer>
  </section>

  <section class="page col-1 row-2">
    <h1 class="page-title">HEADLINE HERE</h1>
    <div class="page-body" style="top:52px">
      <div class="chart-title">USE OF FOUNDER SEED CAPITAL<br>$1.12M SINCE JAN 2014</div>
      <div class="legend"><i style="background:#3d6fb6"></i>marketing <i style="background:var(--orange)"></i>sg&amp;a <i style="background:var(--grey-fill)"></i>r&amp;d <i style="background:var(--gold)"></i>1x legal</div>
      <svg viewBox="0 0 100 76" width="194" height="110" role="img" aria-label="Donut chart: r&amp;d 60%, sg&amp;a 21%, marketing 12%, legal 7%" style="display:block;margin:0 auto">
        <g transform="translate(50 37) rotate(-90)">
          <circle r="28" fill="none" stroke="#ee7a30" stroke-width="14" stroke-dasharray="21.11 175.93" stroke-dashoffset="0"/>
          <circle r="28" fill="none" stroke="#f15a29" stroke-width="14" stroke-dasharray="36.94 175.93" stroke-dashoffset="-21.11"/>
          <circle r="28" fill="none" stroke="#a7a7a7" stroke-width="14" stroke-dasharray="105.56 175.93" stroke-dashoffset="-58.05"/>
          <circle r="28" fill="none" stroke="#fbb03b" stroke-width="14" stroke-dasharray="12.32 175.93" stroke-dashoffset="-163.61"/>
        </g>
        <g font-size="3" fill="#fff" font-family="Open Sans, sans-serif" text-anchor="middle">
          <text x="43.5" y="9.6">legal</text><text x="43.5" y="12.8">7%</text>
          <text x="60.8" y="10.4">marketing</text><text x="60.8" y="13.6">12%</text>
          <text x="77.6" y="32">sg&amp;a</text><text x="77.6" y="35.2">21%</text>
          <text x="29.6" y="55.6">r&amp;d</text><text x="29.6" y="58.8">60%</text>
        </g>
      </svg>
      <div class="h2" style="margin-top:4px">Lorem Ipsum is simply dummy</div>
      <p class="justify">Text of the printing and typesetting industry. Lorem Ipsum has been the industry's standard dummy text ever since the 1500s, when an unknown printer took a galley of type and scrambled it to make a type specimen book. It has survived not only five centuries, but also the leap into electronic typesetting, remaining essentially unchanged. It was popularised in the 1960s with the release of Sheetmark sheets containing Lorem Ipsum passages, and more recently with desktop publishing software like PageSet Pro including versions of Lorem Ipsum.</p>
      <div class="h3">It is a long established fact that</div>
      <p class="justify">A reader will be distracted by the readable content of a page when looking at its layout. The point of using Lorem Ipsum is that it has a more-or-less normal distribution of letters, as opposed to using 'Content here, content here', making it look like readable English. Many desktop publishing packages and web page editors now use Lorem Ipsum as their default model text. Contrary to popular belief, Lorem Ipsum is not simply random text. It has roots in a piece of classical Latin literature from 45 BC, making it over 2000 years old.</p>
    </div>
    <footer class="page-footer"><div class="footer-band">www.velorix.example</div><div class="footer-mark">Velorix</div><div class="page-num">4</div></footer>
  </section>

  <section class="page col-2 row-2">
    <h1 class="page-title">HEADLINE HERE</h1>
    <div class="photo" role="img" aria-label="Photo of a tired businessman at a desk, head in hand" style="position:absolute;left:26px;top:44px;width:88px;height:132px"></div>
    <div class="photo" role="img" aria-label="Photo of a stressed man in a suit leaning over paperwork" style="position:absolute;left:26px;top:198px;width:88px;height:117px"></div>
    <div class="page-body" style="left:124px;right:26px">
      <p class="lead" style="font-size:3.3px">Tallyvo's mission is to help and support the self-employed and small business owners with their administrative tasks so they can focus on what matters – their business.</p>
      <p>Administrative tasks are cumbersome, time-consuming and often prevent small owners from focusing their time and energy on their business and their customers. They can also be extremely stressful and nerve-wracking for those attempting these tasks for the first time.</p>
      <p>At Tallyvo, we envisage accounting for the self-employed and small business owners as being automated and decentralized.</p>
      <p>Accounting can and should be done automatically. By connecting to all sources of accounting data such as bank accounts, payment systems, e-commerce websites and invoicing systems, Tallyvo AI automatically completes these tasks, which would take hours to do manually. Bookings are created automatically and fully completed. Financial statements are available within a couple of clicks, and after analysing your data, Tallyvo AI will offer you tips to improve your financial stability.</p>
      <p>What may seem like a pipedream to the millions of self-employed who struggle with admin.</p>
      <div class="h2">The Tallyvo model</div>
      <p>Tallyvo is based on an innovative license model that uses Token-as-a-License (TaaL). The token represents lifelong software license for Tallyvo solutions. The pre-ICO token sales will enable Tallyvo to complete its development of Tallyvo AI to deliver fully automatic bookkeeping.</p>
    </div>
    <footer class="page-footer"><div class="footer-band">www.velorix.example</div><div class="footer-mark">Velorix</div><div class="page-num">5</div></footer>
  </section>

  <section class="page col-3 row-2">
    <h1 class="page-title">HEADLINE HERE</h1>
    <div class="photo" role="img" aria-label="Photo of a businessman at his laptop, head in hands" style="position:absolute;left:28px;top:44px;width:202px;height:89px"></div>
    <div class="page-body" style="top:138px">
      <p class="lead-bold">Tallyvo's mission is to help and support the self-employed and small business owners with their administrative tasks so they can focus on what matters – their business.</p>
      <p>Administrative tasks are cumbersome, time-consuming and often prevent small owners from focusing their time and energy on their business and their customers. They can also be extremely stressful and nerve-wracking for those attempting these tasks for the first time.</p>
      <p>At Tallyvo, we envisage accounting for the self-employed and small business owners as being automated and decentralized.</p>
      <p>Accounting can and should be done automatically. By connecting to all sources of accounting data such as bank accounts, payment systems, e-commerce websites and invoicing systems, Tallyvo AI automatically completes these tasks, which would take hours to do manually. Bookings are created automatically and statements are available within a couple of clicks, and after analysing your data, Tallyvo AI will offer you tips to improve your financial stability.</p>
      <p>What may seem like a pipedream to the millions of self-employed who struggle with their admin is already a reality. Now is the time to join Tallyvo on its mission to transform the world of bookkeeping through the power of AI.</p>
      <div class="h2">The Tallyvo model</div>
      <p>Tallyvo is based on an innovative license model that uses Token-as-a-License (TaaL). The token represents lifelong software license for Tallyvo solutions. The pre-ICO token sale will enable Tallyvo to complete its development of Tallyvo AI to deliver fully automatic bookkeeping.</p>
      <p>with leading edge business data access to ensure you have the best available data at your fingertips.</p>
    </div>
    <footer class="page-footer"><div class="footer-band">www.velorix.example</div><div class="footer-mark">Velorix</div><div class="page-num">1</div></footer>
  </section>

  <section class="page col-4 row-2">
    <h1 class="page-title">OUR UNDERSTANDING OF YOUR NEEDS</h1>
    <div class="page-body">
      <p>In the last two weeks of January 2014 we conducted high level conversations both with your staff and your technology partner Lumenfield. As a result of those conversations we've been able to gather the following high level goals for your project:</p>
      <div class="h2" style="font-size:5.6px;line-height:1.3">Orbitline must be in place to support Stridewell at launch and as the program evolves</div>
      <p class="lead-bold" style="font-size:3.6px">The most critical aspect of this implementation both in terms of time sensitivity as well as functionality is centered around the support for the Stridewell project. Our current understanding of this project and how it</p>
      <p class="bullet">Stridewell will be comprised of a series of websites focused on organizing institutions and individuals within six specific community sectors with the goal of increased institutional and public support to help the nation become better prepared to minimize the risks and maximize opportunities of changing climate.</p>
      <p class="bullet">The primary goals of the CRM application are:</p>
      <p class="sub-bullet">capture information of individuals and organizations (along with their respective roles)</p>
      <p class="sub-bullet">track their progress on their site specific to-do lists and site interactions</p>
      <p class="sub-bullet">allow Verdancia to push out next steps (ideally in an automated style) related to their to-do list progress and online interactions</p>
      <p class="sub-bullet">infuse Verdancia's online and offline marketing program with useful segmentation information</p>
      <p class="sub-bullet">natively integrate with both the Stridewell family of sites as well as Verdancia's email service provider of choice</p>
      <p class="bullet" style="margin-top:3px">The data architecture must be well defined but flexible to support the core needs of the sites as launch as well as anticipated needs in the future.</p>
      <p class="sub-bullet">For instance, the faith based site may collect a "denomination" field, while other sites may not collect that field.</p>
      <p class="sub-bullet">Future interactions outside of the to-do list may become necessary to track and Verdancia will need a systemic way to capture those interactions, be able to segment on them and potentially provide automated marketing around those similar to the to-do list.</p>
      <p class="bullet" style="margin-top:3px">The information collected from the Stridewell sites must be combined with current information held within Verdancia and provide a holistic view of institutions and individuals.</p>
    </div>
    <footer class="page-footer"><div class="footer-band">www.velorix.example</div><div class="footer-mark">Velorix</div><div class="page-num">1</div></footer>
  </section>

  <section class="page col-1 row-3">
    <h1 class="page-title">BUDGET AND TIMEFRAME</h1>
    <div class="page-body">
      <div class="h2">Implementation Estimate</div>
      <p>The bulk of the implementation costs will be defined by discovery. Based on similar CRM implementation projects, we feel expect that the CRM side will be something between 200 and 300 hours, give or take. The wide swing in hours in phase one is related to the ill-defined nature of both the integration needs and our role in the integration project. Our focus in discovery will be to nail down those requirements and our role as it relates to what is needed to integrate the sites with the CRM.</p>
      <table class="budget">
        <tr><th style="width:52%">Task</th><th>Hours</th><th>Cost</th></tr>
        <tr><td>Discovery</td><td class="c">40</td><td class="c">$8,000</td></tr>
        <tr class="sub"><td>Phase 1</td><td></td><td></td></tr>
        <tr><td>Discovery</td><td class="c">20-40</td><td class="c">$8,000</td></tr>
        <tr><td>Discovery</td><td class="c">20-40</td><td class="c">$8,000</td></tr>
        <tr><td>Discovery</td><td class="c">20-40</td><td class="c">$8,000</td></tr>
        <tr><td>Total Phase 1</td><td class="c">80-240</td><td class="c">$16,800-40,000</td></tr>
        <tr class="sub"><td>Phase 2</td><td></td><td></td></tr>
        <tr><td>Discovery</td><td class="c">20-40</td><td class="c">$8,000</td></tr>
        <tr><td>Total Phase 2</td><td class="c">80-240</td><td class="c">$16,800-40,000</td></tr>
        <tr class="total"><td>Total Estimated Implementation Cost</td><td class="c">220-480</td><td class="c hi">$44,000-96,000</td></tr>
      </table>
      <div class="h2">Project Timeline</div>
      <p>Based on the information we have out our disposal, the March 21st launch date doesn't seem a realistic goal to get both the work done needed to provide the foundation for the future CRM instance and the integration given the state of apparent flux of the requirements. That said, we feel it prudent to proceed with discovery before committing to or pushing that date. We are currently estimating that the first phase will take somewhere between 7 and 12 weeks (including discovery) to complete.</p>
      <table class="budget">
        <tr><th style="width:62%">Task</th><th>Weeks to Complete</th></tr>
        <tr><td>Discovery</td><td class="c">1-2</td></tr>
        <tr><td>Phase 1</td><td class="c">6-10</td></tr>
        <tr><td>Phase 2</td><td class="c">8-12</td></tr>
        <tr class="sub"><td>Total Number of Weeks</td><td></td></tr>
      </table>
    </div>
    <footer class="page-footer"><div class="footer-band">www.velorix.example</div><div class="footer-mark">Velorix</div><div class="page-num">1</div></footer>
  </section>

  <section class="page col-2 row-3 back-cover">
    <svg class="cover-art" viewBox="0 0 250 354" width="250" height="354" aria-hidden="true">
      <defs>
        <linearGradient id="backGrad" x1="0" y1="0" x2="0" y2="1">
          <stop offset="0" stop-color="#f36b2c"/>
          <stop offset="1" stop-color="#ee4a23"/>
        </linearGradient>
      </defs>
      <rect width="250" height="354" fill="#ffffff"/>
      <polygon points="0,0 250,0 250,238 0,286" fill="#f7941d"/>
      <polygon points="0,0 250,0 250,192 0,284" fill="url(#backGrad)"/>
    </svg>
    <div class="brand" style="left:45px;top:307px;font-size:8px">Velorix</div>
    <div class="brand-dot" style="left:80px;top:309px;width:3px;height:3px"></div>
    <div class="contact" style="left:100px;top:306px">
      <div><span class="icon-dot"></span>000-555-0124 Ext 101</div>
      <div><span class="icon-dot"></span>hello@velorix.example</div>
      <div style="padding-left:5px">www.velorix.example</div>
    </div>
    <div class="contact" style="left:150px;top:306px;border-left:.4px solid #999;padding-left:4px">
      <div>300, 1055 Harbour View Street</div>
      <div>Northfield, Columbia A1B 2C3</div>
    </div>
  </section>

</main>
</body>
</html>
```